Wedding Invitation to be used digitally

Design of a Wedding Invitation.
It will be used digitally by whatsapp, so the file format and image size should be appropriate. We don´t intend to print.
Word file with the text contents as attachment. This is REALLY just the text and the main sequencial order of the information that should appear in the invitation.
However, ALL criativity is welcome ofcourse in terms of organization of the information in the paper, font, uppercase and lowercase, numbers and their format, dates and their format, drawings, logo, etc etc

Target Market(s)

family and friends

Requirements
Must have
• A logo at the top with the capitals of our name - R and T
Nice to have
• Should be elegant

```html
<!DOCTYPE html>
<html lang="en">
<head>
<meta charset="utf-8">
<title>Wedding Invitation – Rita &amp; Tomás</title>
<link rel="stylesheet" href="https://fonts.googleapis.com/css2?family=Playfair+Display:wght@400;500&display=swap">
<style>
  :root {
    --backdrop: #efebeb;
    --card: #b09674;
    --ink: #231a12;
    --white: #ffffff;
    --monogram: #86683a;
    --ampersand: #dccab0;
    --frame: rgba(255,255,255,0.7);
    --floral-tone: rgba(190,140,112,0.35);
  }
  html, body {
    margin: 0; padding: 0;
    width: 1200px; height: 854px;
    overflow: hidden;
    background: var(--backdrop);
  }
  .canvas { position: relative; width: 1200px; height: 854px; }
  .invitation {
    position: absolute; left: 361px; top: 110px;
    width: 448px; height: 634px;
    background: var(--card);
    overflow: hidden;
    font-family: "Playfair Display", Georgia, serif;
    color: var(--ink);
  }
  .floral-area {
    position: absolute;
  }
  .floral-area--top {
    left: 0; top: 0; width: 312px; height: 163px;
    background: linear-gradient(160deg, var(--floral-tone), rgba(190,140,112,0) 85%);
  }
  .floral-area--bottom {
    left: 134px; top: 468px; width: 314px; height: 166px;
    background: linear-gradient(340deg, var(--floral-tone), rgba(190,140,112,0) 85%);
  }
  .frame { position: absolute; left: 0; top: 0; }
  .monogram {
    position: absolute; left: 0; width: 448px; top: 116px;
    margin: 0;
    text-align: center;
    font-size: 104px; line-height: 1;
    color: var(--monogram);
    letter-spacing: 4px;
    transform: translateY(-50%);
  }
  .line {
    position: absolute; left: 0; width: 448px;
    text-align: center; margin: 0;
    white-space: nowrap;
    line-height: 1;
    transform: translateY(-50%);
  }
  .eyebrow { font-size: 11px; letter-spacing: 2.2px; }
  .eyebrow--invite { letter-spacing: 1.2px; }
  .name { font-size: 37px; color: var(--white); z-index: 2; }
  .ampersand { font-size: 96px; color: var(--ampersand); z-index: 1; }
  .divider {
    position: absolute; left: 194px; top: 391px;
    width: 60px; height: 2px; background: var(--white);
  }
  .date { font-size: 15.5px; }
  .detail { font-size: 10.8px; }
  .rsvp {
    position: absolute; left: 26px; top: 601px;
    transform: translateY(-50%);
    font-size: 11px; letter-spacing: 1.3px; color: var(--white);
    line-height: 1; margin: 0;
  }
</style>
</head>
<body>
<div class="canvas">
  <article class="invitation">
    <div class="floral-area floral-area--top" role="img" aria-label="Watercolour roses with leaves in the top corner"></div>
    <div class="floral-area floral-area--bottom" role="img" aria-label="Watercolour roses with leaves in the bottom corner"></div>

    <svg class="frame" width="448" height="634" viewBox="0 0 448 634" aria-hidden="true">
      <path d="M148 106 H31 V571 H417 V106 H312" fill="none" stroke="var(--frame)" stroke-width="0.8"/>
    </svg>

    <p class="monogram">R T</p>

    <p class="line eyebrow" style="top:225px">TOGETHER WITH THEIR FAMILIES</p>
    <p class="line ampersand" style="top:296px">&amp;</p>
    <p class="line name" style="top:258px">RITA LOBO</p>
    <p class="line name" style="top:327px">TOMÁS VIEGAS</p>
    <p class="line eyebrow eyebrow--invite" style="top:367px">INVITE YOU TO THEIR WEDDING CELEBRATION</p>

    <div class="divider"></div>

    <p class="line date" style="top:417px">SUNDAY, JULY 28, 2024</p>
    <p class="line date" style="top:434px">AT 11h30</p>

    <p class="line detail" style="top:460px">CAPELA DE SANTA LUZIA | COSTA AZUL</p>
    <p class="line detail" style="top:473px">(PARKING – MARINA VELHA OR PARQUE TERRA MAR)</p>
    <p class="line detail" style="top:498px">RECEPTION TO FOLLOW</p>
    <p class="line detail" style="top:523px">AT</p>
    <p class="line detail" style="top:536px">HOTEL FORTE DA ENSEADA | COSTA AZUL</p>
    <p class="line detail" style="top:548px">(PARKING – ON SITE)</p>

    <p class="rsvp">RSVP BY 20TH JULY</p>
  </article>
</div>
</body>
</html>
```